Corvells Finest 4 years in a row

I need a billboard that has all the attached logos and says:

Corvell's Finest Realtor 4 Years in a row!

1.75 Listing Fee

Tobias Wrenfield

410-555-0147

and somewhere very small at the bottom:

833-555-0192

2947 W Pennlow Rd, Bel Air, MD 21099

I put in the last winner just to give an idea of what I'm looking for, although I'd like to switch it up a little bit.

```html
<!DOCTYPE html>
<html lang="en">
<head>
<meta charset="utf-8">
<title>Tobias Wrenfield Billboard</title>
<link rel="stylesheet" href="https://fonts.googleapis.com/css2?family=Anton&family=Poppins:wght@400;500&display=swap">
<style>
  :root {
    --navy: #15305e;
    --ink: #111111;
    --white: #ffffff;
    --panel-grey: #d3d7dc;
    --facet-grey: #e4e7ea;
    --pill-fill: #e8ecf2;
    --badge-dark: #2b2522;
    --badge-darker: #1f1a18;
    --stage-top: #e9eaec;
    --stage-bottom: #d9dbde;
  }
  html, body {
    margin: 0;
    padding: 0;
    width: 1059px;
    height: 1200px;
    overflow: hidden;
  }
  body {
    position: relative;
    background: linear-gradient(180deg, var(--stage-top), var(--stage-bottom));
  }
  .billboard {
    position: absolute;
    left: 40px;
    top: 457px;
    width: 980px;
    height: 286px;
    box-shadow: 0 10px 24px rgba(0, 0, 0, 0.28);
    display: block;
  }
  .headline-kicker {
    font-family: "Poppins", sans-serif;
    font-weight: 500;
    font-size: 27px;
    letter-spacing: 7px;
    fill: var(--ink);
  }
  .headline-streak,
  .agent-name,
  .phone-number,
  .fee-rate,
  .contact-label {
    font-family: "Anton", sans-serif;
  }
  .headline-streak { font-size: 31px; fill: var(--navy); }
  .agent-name { font-size: 124px; fill: var(--navy); }
  .phone-number { font-size: 108px; fill: var(--navy); }
  .fee-rate { font-size: 30px; fill: var(--white); }
  .fee-label {
    font-family: "Poppins", sans-serif;
    font-size: 25px;
    letter-spacing: 6px;
    fill: var(--navy);
  }
  .contact-label { font-size: 30px; }
  .contact-label.on-navy { fill: var(--white); }
  .contact-label.on-light { fill: var(--navy); }
  .team-name {
    font-family: "Anton", sans-serif;
    font-size: 36px;
    letter-spacing: 2px;
    fill: var(--navy);
  }
  .footer-text {
    font-family: "Poppins", sans-serif;
    font-size: 16px;
    letter-spacing: 2.4px;
    fill: var(--white);
  }
</style>
</head>
<body>
<svg class="billboard" viewBox="0 0 1584 462" xmlns="http://www.w3.org/2000/svg">
  <defs>
    <linearGradient id="portrait-tone" x1="0" y1="0" x2="0" y2="1">
      <stop offset="0" stop-color="#c9a48c"/>
      <stop offset="0.3" stop-color="#9aa3b3"/>
      <stop offset="1" stop-color="#1f2c47"/>
    </linearGradient>
  </defs>

  <rect class="board-ground" width="1584" height="462" fill="var(--white)"/>

  <g class="backdrop-facets">
    <polygon points="1250,0 1584,0 1584,405 1190,405 935,90 1170,80" fill="var(--panel-grey)"/>
    <polygon points="1330,0 1500,0 1420,110" fill="var(--facet-grey)"/>
    <polygon points="1500,0 1584,0 1584,120" fill="var(--facet-grey)"/>
    <polygon points="1040,95 1180,85 1260,200" fill="var(--facet-grey)"/>
  </g>

  <g class="team-mark">
    <circle cx="175" cy="95" r="34" fill="var(--navy)"/>
    <text class="team-name" x="175" y="192" text-anchor="middle">THE SUMMIT GROUP</text>
  </g>

  <g class="award-badges">
    <circle cx="282" cy="300" r="42" fill="var(--badge-darker)"/>
    <circle cx="243" cy="302" r="52" fill="var(--badge-dark)"/>
    <circle cx="192" cy="305" r="60" fill="var(--badge-darker)"/>
    <circle cx="122" cy="308" r="70" fill="var(--badge-dark)"/>
  </g>

  <g class="headline">
    <text class="headline-kicker" x="790" y="46" text-anchor="middle">CORVELL'S FINEST REALTOR</text>
    <text class="headline-streak" x="790" y="88" text-anchor="middle">4 YEARS IN A ROW!</text>
    <text class="agent-name" x="388" y="212" textLength="810" lengthAdjust="spacingAndGlyphs">TOBIAS WRENFIELD</text>
  </g>

  <g class="listing-fee">
    <rect x="622" y="230" width="340" height="48" rx="7" fill="var(--pill-fill)" stroke="var(--navy)" stroke-width="2"/>
    <path d="M629 230 H734 V278 H629 A7 7 0 0 1 622 271 V237 A7 7 0 0 1 629 230 Z" fill="var(--navy)"/>
    <text class="fee-rate" x="678" y="266" text-anchor="middle">1.75%</text>
    <text class="fee-label" x="848" y="264" text-anchor="middle">LISTING FEE</text>
  </g>

  <g class="call-line">
    <rect x="472" y="300" width="88" height="90" rx="7" fill="var(--pill-fill)" stroke="var(--navy)" stroke-width="2"/>
    <path d="M479 300 H553 A7 7 0 0 1 560 307 V345 H472 V307 A7 7 0 0 1 479 300 Z" fill="var(--navy)"/>
    <text class="contact-label on-navy" x="516" y="337" text-anchor="middle">CALL</text>
    <text class="contact-label on-light" x="516" y="380" text-anchor="middle">TEXT</text>
    <text class="phone-number" x="578" y="388" textLength="537" lengthAdjust="spacingAndGlyphs">410-555-0147</text>
  </g>

  <g class="footer-band">
    <polygon points="0,405 1300,405 1300,462 0,462" fill="var(--navy)"/>
    <text class="footer-text" x="28" y="440">833-555-0192</text>
    <text class="footer-text" x="232" y="440">|</text>
    <text class="footer-text" x="290" y="440">2947 W Pennlow Rd, Bel Air, MD 21099</text>
    <text class="footer-text" x="772" y="440">|</text>
    <text class="footer-text" x="830" y="440">www.summitgroupsells.com</text>
  </g>

  <g class="agent-portrait" role="img" aria-label="Portrait photo of the realtor in a navy suit">
    <path d="M1290 462 L1300 250 Q1330 200 1390 180 L1380 60 Q1430 10 1480 60 L1480 180 Q1540 200 1555 250 L1560 462 Z" fill="url(#portrait-tone)"/>
  </g>
</svg>
</body>
</html>
```